Velmora Investment Management Needs Door Wording Design

We need someone to put together a design for our glass front doors (2).

The words could be, but aren't limited to, as follows:

"100
Serenely Restorative Bodywork
*Ring Bell"

and

"200 & 300
Velmora Investment Management inc.
*Ring Bell"

The design should be clean, subtle and professional. It is a simple mainly glass door with a black frame. Our website is www.velmorainvest.ca for a more detailed description of what we do. The adjacent business would also be involved, as per the wording of the Serenely Restorative Bodywork.

We are looking for something to bring out the wording on the door (there is currently a piece of paper printed and taped to the inside).

Dimensions of the window are 47 inches x 23 inches.

Thanks!

Colors
000000
ffffff

Requirements
Must have
• The previous words
Nice to have
• Creative flair, taking into consideration the nature of our business (Investment Management)

```html
<!DOCTYPE html>
<html lang="en">
<head>
<meta charset="utf-8">
<title>Velmora Investment Management – Door Lettering</title>
<link rel="stylesheet" href="https://fonts.googleapis.com/css2?family=Oswald:wght@500&family=Roboto+Condensed:wght@700&display=swap">
<style>
  :root {
    --glass-top: #5b6478;
    --glass-bottom: #26313d;
    --vinyl: #ffffff;
    --ink: #2b3442;
  }
  html, body {
    margin: 0;
    padding: 0;
    width: 1200px;
    height: 1054px;
    overflow: hidden;
  }
  body {
    background: linear-gradient(180deg, var(--glass-top) 0%, #3e4859 45%, var(--glass-bottom) 100%);
    position: relative;
  }
  .door-decal {
    position: absolute;
    left: 177px;
    top: 104px;
    width: 846px;
    height: 846px;
    box-sizing: border-box;
    border: 75px solid var(--vinyl);
    border-bottom-width: 78px;
  }
  .decal-panel {
    position: absolute;
    inset: 0;
    display: flex;
    flex-direction: column;
    align-items: center;
    color: var(--vinyl);
    text-align: center;
  }
  .suite-numbers {
    margin-top: 62px;
    font-family: "Roboto Condensed", "Arial Narrow", sans-serif;
    font-weight: 700;
    font-size: 96px;
    line-height: 1;
  }
  .company-name {
    margin-top: 56px;
    font-family: "Roboto Condensed", "Arial Narrow", sans-serif;
    font-weight: 700;
    font-size: 150px;
    line-height: 1;
    letter-spacing: 1px;
  }
  .company-line {
    margin-top: 64px;
    font-family: "Oswald", "Arial Narrow", sans-serif;
    font-weight: 500;
    font-size: 66px;
    line-height: 1;
    transform: scaleX(0.84);
    white-space: nowrap;
  }
  .company-suffix {
    margin-top: 16px;
    font-family: "Oswald", "Arial Narrow", sans-serif;
    font-weight: 500;
    font-size: 34px;
    line-height: 1;
  }
  .ring-bell {
    position: absolute;
    left: 0;
    right: 0;
    bottom: -72px;
    text-align: center;
    font-family: "Roboto Condensed", "Arial Narrow", sans-serif;
    font-weight: 700;
    font-size: 54px;
    line-height: 1;
    color: var(--ink);
  }
</style>
</head>
<body>
  <div class="door-decal">
    <div class="decal-panel">
      <div class="suite-numbers">200 &amp; 300</div>
      <div class="company-name">VELMORA</div>
      <div class="company-line">INVESTMENT MANAGEMENT</div>
      <div class="company-suffix">INC.</div>
    </div>
    <div class="ring-bell">*Ring Bell</div>
  </div>
</body>
</html>
```